VornaDerm/The experts in permanent hairremoval

Our Brand is VornaDerm and we are specialized on permantent hair removal for the body for men and woman. VornaDerm is working as a Franchise chain.
The brand should be positioned as lifestyle brand but with a medical background. People should trust in us. We take care about their body. This need to be communicated 100%.
Our system is inexpensive but we don't want to show that we are cheap. So we want to communicate that permanent hair removal is a real lifestyle product but affordable.
We already created a logo that you can see the style and colour we prefer.

Target Market(s)

Europe beginning (especially german spoken markets), Middle East, Africa

Industry/Entity Type

Hair Removal

Number of Pages Required

5+ page

Font styles to use
Serif
Other font styles liked:
• Trajan Pro

Requirements
Nice to have
• We are very open for new ideas

```html
<!DOCTYPE html>
<html lang="en">
<head>
<meta charset="utf-8">
<title>VornaDerm – Permanent Hair Removal</title>
<link href="https://fonts.googleapis.com/css2?family=Lato:ital,wght@0,300;0,400;0,700;0,900;1,300&family=Libre+Baskerville&display=swap" rel="stylesheet">
<style>
  :root {
    --sky: #56b1e3;
    --teal: #1c9a8a;
    --ink: #333a40;
    --muted: #6f7276;
    --rule: #4a4d52;
    --footer: #7b7c80;
    --paper: #ffffff;
    --hero-light: #f4f4f4;
  }
  * { margin: 0; padding: 0; box-sizing: border-box; }
  html, body { width: 890px; height: 1200px; overflow: hidden; background: var(--paper); }
  body { position: relative; font-family: "Lato", sans-serif; color: var(--ink); }

  .topbar { position: absolute; left: 0; top: 0; width: 890px; height: 30px; background: var(--sky); color: #fff; font-size: 7px; letter-spacing: .5px; }
  .topbar .contact { position: absolute; left: 80px; top: 11px; }
  .topbar .contact b { font-weight: 900; margin-right: 8px; }
  .topbar .contact .mail { text-decoration: underline; }
  .topbar .account { position: absolute; right: 78px; top: 11px; font-weight: 900; letter-spacing: 1.2px; }

  .header { position: absolute; left: 0; top: 30px; width: 890px; height: 82px; }
  .brand { position: absolute; left: 40px; top: 26px; display: flex; align-items: center; gap: 8px; font-size: 24px; font-weight: 400; color: var(--sky); }
  .brand .dot { width: 10px; height: 10px; border-radius: 50%; background: var(--sky); }
  .nav { position: absolute; left: 240px; top: 36px; display: flex; gap: 31px; font-size: 8.5px; font-weight: 700; letter-spacing: 1.2px; color: #3c4147; }
  .nav .active { color: var(--sky); border-bottom: 1px solid var(--sky); padding: 0 5px 3px; margin-top: 0; }
  .tools { position: absolute; left: 753px; top: 28px; display: flex; gap: 9px; }
  .tools span { width: 24px; height: 24px; border-radius: 50%; background: #7d7f83; display: flex; align-items: center; justify-content: center; }

  .hero { position: absolute; left: 0; top: 112px; width: 890px; height: 354px; background: linear-gradient(90deg, #f7f7f7 0%, #ededed 55%, #e4e4e4 100%); overflow: hidden; }
  .hero-photo { position: absolute; left: 500px; top: 0; width: 390px; height: 354px; background: linear-gradient(110deg, #e9e9e9 0%, #8a5b45 22%, #c99a83 55%, #e2b9a3 80%, #f0e2da 100%); }
  .hero-copy { position: absolute; left: 196px; top: 62px; width: 210px; }
  .hero-copy .kicker { font-size: 15px; font-weight: 300; color: #6a6d70; letter-spacing: .2px; }
  .hero-copy h1 { font-family: "Libre Baskerville", serif; font-weight: 400; font-size: 34px; color: var(--teal); line-height: 1.15; margin-top: 2px; letter-spacing: -.5px; padding-bottom: 10px; border-bottom: 1px solid #cfcfcf; }
  .hero-copy p { font-size: 16px; font-weight: 300; font-style: italic; color: #6a6d70; line-height: 23px; margin-top: 12px; }

  .section-title { position: absolute; left: 0; top: 498px; width: 890px; text-align: center; font-size: 22px; font-weight: 400; color: #6d6f72; letter-spacing: .8px; }
  .divider { position: absolute; left: 0; width: 890px; height: 10px; }

  .intro { position: absolute; left: 78px; top: 580px; width: 745px; font-size: 12.3px; line-height: 18.2px; letter-spacing: .35px; color: #3a3f44; }

  .areas { position: absolute; left: 76px; top: 720px; width: 760px; display: grid; grid-template-columns: 282px 282px 196px; row-gap: 11px; }
  .area { display: flex; align-items: center; gap: 22px; font-size: 11.5px; font-weight: 700; letter-spacing: .5px; color: #2e3338; height: 25px; }
  .area::before { content: ""; width: 25px; height: 25px; border-radius: 50%; background: var(--sky); flex: none; }

  .cards { position: absolute; left: 98px; top: 821px; display: flex; gap: 18px; }
  .card { width: 220px; }
  .card .frame { width: 220px; height: 145px; border: 1.5px solid #222; }
  .card .caption { margin-top: 9px; display: flex; align-items: center; justify-content: center; gap: 10px; font-size: 12.5px; font-weight: 700; letter-spacing: 1.3px; color: #4a4e53; }
  .card .caption::before, .card .caption::after { content: ""; width: 30px; height: 1px; background: #4a4e53; }
  .photo-products { background: linear-gradient(135deg, #f4f4f4, #c9ccd0 45%, #3b5b85 70%, #b3252f); }
  .photo-gift { background: radial-gradient(circle at 50% 55%, #f4f0ee 0%, #e3b5a9 45%, #b41e3a 65%, #fdf9f8 90%); }
  .photo-map { background: linear-gradient(135deg, #e8e4dc, #f0c46a 50%, #e8e4dc); }

  .footer { position: absolute; left: 0; top: 1046px; width: 890px; height: 119px; background: var(--footer); }
  .newsletter { position: absolute; left: 304px; top: 45px; display: flex; }
  .newsletter .field { width: 198px; height: 29px; background: #fff; font-size: 10px; color: #555; padding: 9px 0 0 15px; letter-spacing: .4px; }
  .newsletter .btn { width: 83px; height: 29px; background: #e6e6e6; font-size: 7.5px; font-weight: 900; letter-spacing: 1px; color: #3d4146; text-align: center; padding-top: 10px; }
  .bottombar { position: absolute; left: 0; top: 1165px; width: 890px; height: 35px; background: var(--sky); color: #fff; font-size: 8px; letter-spacing: .5px; text-align: center; padding-top: 13px; }
</style>
</head>
<body>

<div class="topbar">
  <div class="contact"><b>CONTACT US:</b> + 7 (800) 555 01 42 &nbsp;&nbsp;|&nbsp;&nbsp; <span class="mail">hello@vornaderm-mail.com</span></div>
  <div class="account">LOG IN &nbsp;&nbsp;&nbsp; | &nbsp;&nbsp;&nbsp; REGISTER</div>
</div>

<header class="header">
  <div class="brand"><span class="dot"></span>VornaDerm</div>
  <nav class="nav">
    <span>HOME</span><span>PRICES</span><span class="active">APPOINMENTS</span><span>ABOUT</span><span>JOBS &amp; CAREERS</span><span>FRANCHIS</span>
  </nav>
  <div class="tools">
    <span><svg width="10" height="9" viewBox="0 0 10 9"><path d="M0 1h2l1.3 4.5h5L9.5 2H2.6" fill="none" stroke="#fff" stroke-width="1"/><circle cx="4" cy="7.6" r=".9" fill="#fff"/><circle cx="7.6" cy="7.6" r=".9" fill="#fff"/></svg></span>
    <span><svg width="9" height="9" viewBox="0 0 9 9"><circle cx="3.6" cy="3.6" r="2.6" fill="none" stroke="#fff" stroke-width="1.1"/><path d="M5.6 5.6L8.3 8.3" stroke="#fff" stroke-width="1.2"/></svg></span>
  </div>
</header>

<section class="hero">
  <div class="hero-photo" role="img" aria-label="Portrait photograph of a woman with long brown hair touching her cheek"></div>
  <div class="hero-copy">
    <div class="kicker">GENTLE &amp; PERMANENT</div>
    <h1>Hair Removal</h1>
    <p>Performed by a Professional, Licensed Electrologist.</p>
  </div>
</section>

<h2 class="section-title">Hair Removal Applications</h2>
<svg class="divider" style="top:544px" viewBox="0 0 890 10">
  <line x1="0" y1="5" x2="420" y2="5" stroke="var(--rule)" stroke-width="1"/>
  <circle cx="430" cy="5" r="3" fill="none" stroke="#222" stroke-width="1.3"/>
  <circle cx="462" cy="5" r="3" fill="none" stroke="#222" stroke-width="1.3"/>
  <line x1="473" y1="5" x2="890" y2="5" stroke="var(--rule)" stroke-width="1"/>
</svg>

<p class="intro">ClearPulse™ safely and effectively treats all skin types including tanned skin. For darker skin types and people with tans, appropriate fluences are generally lower and appropriate pulse widths are generally longer to prevent damage to the epidermis. Using the appropriate treatment parameters, people with all skin types can benefit from laser hair removal with the ClearPulse™. Virtually any area with dark hair excluding areas very close to the eyes can be treated. The following areas are treated frequently for both men and woman:</p>

<div class="areas">
  <div class="area">Facial Hair</div>
  <div class="area">Bikini and Underarms</div>
  <div class="area">Chest and Back</div>
  <div class="area">Legs and Arms</div>
  <div class="area">Fingers and Toes</div>
  <div class="area">Areas of Unwanted Hair</div>
</div>

<svg class="divider" style="top:795px" viewBox="0 0 890 10">
  <line x1="0" y1="5" x2="420" y2="5" stroke="var(--rule)" stroke-width="1"/>
  <circle cx="430" cy="5" r="3" fill="none" stroke="#222" stroke-width="1.3"/>
  <circle cx="462" cy="5" r="3" fill="none" stroke="#222" stroke-width="1.3"/>
  <line x1="473" y1="5" x2="890" y2="5" stroke="var(--rule)" stroke-width="1"/>
</svg>

<div class="cards">
  <div class="card">
    <div class="frame photo-products" role="img" aria-label="Photograph of skincare bottles and tubes"></div>
    <div class="caption">Accessories</div>
  </div>
  <div class="card">
    <div class="frame photo-gift" role="img" aria-label="Illustration of a white gift box with a red ribbon bow"></div>
    <div class="caption">Gift cards</div>
  </div>
  <div class="card">
    <div class="frame photo-map" role="img" aria-label="Street map showing the salon location"></div>
    <div class="caption">Visit us</div>
  </div>
</div>

<footer class="footer">
  <div class="newsletter">
    <div class="field">I want your newsletters!</div>
    <div class="btn">SUBSCRIBE</div>
  </div>
</footer>
<div class="bottombar">Copyright 2015 | All rights reserved</div>

</body>
</html>
```